Marwell Herd Services concrete grooving services flyer design

Marwell Herd Services offers 4 different grooving options:

DEEP GROOVING
, ideal for Safety & Efficiency
Our hugely popular deep straight line grooving, long lasting, minimal hoof wear,

Create safe and secure flooring, cows walk without hesitation

Achieve groove spacing for optimal hoof function, reduce hoof trauma

Ideal grooves to new concrete or surfaces with little to no pattern or previous grooving

Ideal groove pattern as promoted by The pasturewide programme

MINI GROOVING,
Smaller dimensions Ideal option for heifer housing and high activity areas such as parlours and handling areas

An ideal solution for regaining traction on old previous grooving that has lost its traction without loosing stability

Plaining

smoothing down rough concrete with previous aggressive grooving or patterns to reduce hoof trauma & wear

SENSOR PLATE SINKING

sinking sensor plates for automated machines below surface level preventing accidental damage & wear

```html
<!DOCTYPE html>
<html lang="en">
<head>
<meta charset="utf-8">
<title>Marwell Herd Services – Concrete Grooving Services</title>
<link rel="stylesheet" href="https://fonts.googleapis.com/css2?family=Open+Sans:wght@400;600;700;800&family=Source+Sans+3:wght@400;600&display=swap">
<style>
:root{
  --amber:#f0b12a;
  --amber-deep:#e8a81f;
  --footer:#c39a34;
  --ink:#111111;
  --text:#1d1d1d;
  --paper:#ffffff;
  --mist:#ecebe8;
  --mist-dark:#dcdad5;
  --line:#5a5a5a;
}
*{margin:0;padding:0;box-sizing:border-box}
html,body{width:837px;height:1200px;overflow:hidden;background:var(--paper)}
.flyer{position:relative;width:837px;height:1200px;overflow:hidden;
  background:linear-gradient(90deg,var(--mist) 0,var(--mist-dark) 446px,var(--amber) 446px,var(--amber-deep) 837px);
  font-family:"Source Sans 3",Arial,sans-serif;color:var(--text)}
.backdrop{position:absolute;left:0;top:0;width:837px;height:1156px}
.brand{position:absolute;left:28px;top:42px;display:flex;align-items:center;gap:8px}
.brand-dot{width:26px;height:26px;border-radius:50%;background:var(--ink)}
.brand-name{font-family:"Source Sans 3",Arial,sans-serif;font-weight:600;font-size:17px;line-height:19px;color:var(--ink);width:100px}
.headline{position:absolute;left:16px;top:280px;font-family:"Open Sans",Arial,sans-serif;font-weight:800;font-size:30px;line-height:37px;letter-spacing:3.5px;color:var(--ink)}
.service-photo{position:absolute;width:182px;height:182px;border-radius:50%;border:6px solid var(--paper)}
.photo-deep{left:99px;top:476px;background:radial-gradient(circle at 50% 30%,#c9b07a,#9c7a2c 60%,#6d5520)}
.photo-sensor{left:541px;top:476px;background:radial-gradient(circle at 50% 60%,#8a8a86,#5b574f 55%,#35322c)}
.photo-mini{left:99px;top:839px;background:linear-gradient(160deg,#6e6a63,#a39f97 50%,#4d4a45)}
.photo-plain{left:531px;top:839px;background:linear-gradient(180deg,#7a6f66,#a7a19a 45%,#5c5853)}
.pill{position:absolute;height:45px;width:333px;border-radius:23px;background:var(--paper);
  font-family:"Open Sans",Arial,sans-serif;font-weight:700;font-size:18px;letter-spacing:-.2px;color:var(--ink);
  display:flex;align-items:center;justify-content:center}
.pill-deep{left:24px;top:630px}
.pill-sensor{left:480px;top:630px}
.pill-mini{left:22px;top:993px}
.pill-plain{left:464px;top:993px}
.tagline{position:absolute;left:28px;top:679px;font-size:14.5px;letter-spacing:1.6px;color:var(--ink)}
.points{position:absolute;list-style:none;font-size:13.6px;line-height:16.6px;color:var(--text)}
.points li{position:relative;padding-left:16px}
.points li::before{content:"";position:absolute;left:0;top:3px;border-left:9px solid var(--paper);border-top:5px solid transparent;border-bottom:5px solid transparent}
.points-deep{left:28px;top:704px;width:412px;font-size:13.4px}
.points-sensor{left:453px;top:688px;width:370px}
.points-sensor li{padding-left:24px}
.points-mini{left:29px;top:1053px;width:335px}
.points-plain{left:452px;top:1053px;width:340px;font-size:15px;line-height:19px}
.footer{position:absolute;left:0;top:1156px;width:837px;height:44px;background:var(--footer);
  display:flex;align-items:center;justify-content:center;gap:20px;color:#f5f0e4;font-size:16.5px;letter-spacing:.3px}
.footer-item{display:flex;align-items:center;gap:9px}
.footer svg{width:17px;height:17px}
</style>
</head>
<body>
<div class="flyer">
  <svg class="backdrop" viewBox="0 0 837 1156">
    <defs>
      <linearGradient id="barnTone" x1="0" y1="0" x2="0.4" y2="1">
        <stop offset="0" stop-color="#b7b3aa"/>
        <stop offset=".45" stop-color="#b48a3a"/>
        <stop offset="1" stop-color="#d39a2a"/>
      </linearGradient>
    </defs>
    <path role="img" aria-label="Photo of a grooving machine cutting lines into a wet concrete barn floor"
      d="M0,0 H837 V300 Q760,470 560,495 Q330,505 175,360 L0,230 Z" fill="url(#barnTone)"/>
    <circle cx="95" cy="316" r="138" fill="#ffffff"/>
    <path d="M0,232 Q120,130 200,170 Q250,200 238,300" fill="none" stroke="var(--line)" stroke-width="1"/>
    <line x1="0" y1="565" x2="185" y2="380" stroke="var(--line)" stroke-width="1"/>
    <g transform="translate(693,251) rotate(-47)">
      <rect x="-205" y="-38" width="410" height="76" rx="38" fill="var(--amber)"/>
      <text x="0" y="8" text-anchor="middle" font-family="Open Sans, Arial, sans-serif" font-size="21" letter-spacing="4" fill="#1a1a1a">CONCRETE GROOVING SERVICES</text>
    </g>
  </svg>

  <div class="brand"><span class="brand-dot"></span><span class="brand-name">Marwell Herd Services</span></div>

  <h1 class="headline">4 SERVICES<br>OFFERED :</h1>

  <div class="service-photo photo-deep" role="img" aria-label="Photo of deep parallel grooves across a barn floor"></div>
  <div class="service-photo photo-sensor" role="img" aria-label="Photo of a sinking machine in a cow barn beside the feed lane"></div>
  <div class="service-photo photo-mini" role="img" aria-label="Photo of close-up mini grooved concrete"></div>
  <div class="service-photo photo-plain" role="img" aria-label="Photo of a planing machine smoothing a concrete strip"></div>

  <div class="pill pill-deep">1. DEEP GROOVING</div>
  <div class="pill pill-sensor">2. SENSOR PLATE SINKING</div>
  <div class="pill pill-mini">3. MINI GROOVING</div>
  <div class="pill pill-plain">4. PLAINING</div>

  <p class="tagline">ideal for Safety &amp; Efficiency</p>
  <ul class="points points-deep">
    <li>Our hugely popular deep straight line grooving, long lasting,<br>minimal hoof wear.</li>
    <li>Create safe and secure flooring, cows walk without hesitation</li>
    <li>Achieve groove spacing for optimal hoof function,<br>reduce hoof trauma</li>
    <li>Ideal grooves to new concrete or surfaces with little to no<br>pattern or previous grooving</li>
    <li>Ideal groove pattern as promoted by The pasturewide programme</li>
  </ul>

  <ul class="points points-sensor">
    <li>Sinking sensor plates for automated machines below surface level</li>
    <li>Preventing accidental damage &amp; wear</li>
  </ul>

  <ul class="points points-mini">
    <li>Smaller dimensions Ideal option for heifer housing and high activity areas such as parlours and handling areas</li>
    <li>An ideal solution for regaining traction on old previous grooving that has lost its traction without loosing stability</li>
  </ul>

  <ul class="points points-plain">
    <li>Smoothing down rough concrete with previous aggressive grooving or patterns to reduce hoof trauma &amp; wear</li>
  </ul>

  <footer class="footer">
    <span class="footer-item">
      <svg viewBox="0 0 24 24" fill="none" stroke="currentColor" stroke-width="1.5"><circle cx="12" cy="12" r="11"/><path d="M8 6.5l2 2.5-1 1.5c.8 1.8 2.2 3.2 4 4l1.5-1 2.5 2-1 2c-4.5-.5-8.5-4.5-9-9z"/></svg>
      CALL NOW : +000 4821 3390
    </span>
    <span class="footer-item">
      <svg viewBox="0 0 24 24" fill="none" stroke="currentColor" stroke-width="1.5"><circle cx="12" cy="12" r="10"/><ellipse cx="12" cy="12" rx="4.5" ry="10"/><line x1="2" y1="12" x2="22" y2="12"/><path d="M4 7h16M4 17h16"/></svg>
      www.marwellherd.example
    </span>
  </footer>
</div>
</body>
</html>
```